Corvalux 4", 6", 8" QM pumps catalog

A professional clean looking work.

Please put the file named "Write up" for the full description.

For this project, we want the portrait landscape.
Please based the front and back cover design on the two previous jobs, files marked as “Previous Job 1 and Job 2” It will be appreciated if you can come up with two alternatives for the covers: one design on each previous job design
You are free to change the design a little bit so that it is slightly different from the previous job but not too much so that there are still “similarities” and corporate identity.
For the inserts, you are free to deviate from the two previous jobs.
Colors used bright yellow Pantone 803C and dark grey instead of black.
Wordings are all either black or white, not dark grey
Please design the catalog with CYMCK and not with Pantone.

Reason: Expect the finalization of at least the front and back cover by 11th of November. 11th to 17th is for the finalization of the inserts Dateline required by the 17th and not 22nd as we need the works to be printed on time for the exhibition

Dear Designers, Please submit your front and back cover designs at the earliest

Requirements
Must have
• Clean, professional look, portrait orientation
• Corporate yellow color and dark grey colours used.
• Wordings in black color
• Design in CYMCK and not in pantone
Nice to have
• Some corporate identity with the previous 2 jobs especially for the front and back cover. For the Inserts - you are free to deviate
Should not have
• Messy

```html
<!DOCTYPE html>
<html lang="en">
<head>
<meta charset="utf-8">
<title>Corvalux 4" QM Pumps Series – Cross Sectional Drawing</title>
<link href="https://fonts.googleapis.com/css2?family=Anton&family=Arimo:wght@400&family=Questrial&family=Playfair+Display:ital,wght@1,900&display=swap" rel="stylesheet">
<style>
  :root {
    --yellow: #fde725;
    --dark: #111111;
    --ink: #111111;
    --row-grey: #e4e4e4;
    --rule: #8a8a8a;
    --paper: #ffffff;
    --drawing: #ececec;
  }
  * { margin: 0; padding: 0; box-sizing: border-box; }
  html, body { width: 848px; height: 1200px; overflow: hidden; background: var(--paper); }
  .page { position: relative; width: 848px; height: 1200px; background: var(--paper); font-family: "Arimo", Arial, sans-serif; color: var(--ink); }

  .header-series, .header-title {
    position: absolute; top: 53px; height: 64px;
    display: flex; align-items: center; justify-content: center;
    font-family: "Anton", "Impact", sans-serif; font-size: 22px; letter-spacing: 0.3px;
  }
  .header-series { left: 0; width: 316px; background: var(--yellow); color: var(--ink); }
  .header-title { left: 326px; width: 522px; background: var(--dark); color: var(--yellow); }

  .section-drawing {
    position: absolute; left: 44px; top: 172px; width: 316px; height: 948px;
    background: linear-gradient(180deg, #f2f2f2, #e2e2e2);
    border: 1px solid #bdbdbd;
  }

  .spec { position: absolute; left: 380px; top: 366px; width: 410px; }
  .spec-title {
    font-family: "Questrial", "Century Gothic", sans-serif; font-size: 26.5px;
    text-align: center; padding-left: 14px; line-height: 32px;
    border-bottom: 1px solid var(--rule); padding-bottom: 2px;
  }
  .spec-table { width: 408px; border-collapse: separate; border-spacing: 0; margin-top: 7px; font-size: 12.4px; }
  .spec-table th {
    background: var(--dark); color: #fff; font-weight: 400; height: 20px;
    border-left: 8px solid var(--paper);
  }
  .spec-table th:first-child { border-left: 0; }
  .spec-table td { height: 23.2px; vertical-align: middle; }
  .spec-table tr.shaded td { background: var(--row-grey); }
  .spec-table td.pos { width: 41px; text-align: center; }
  .spec-table td.comp { padding-left: 17px; width: 172px; }
  .spec-table td.mat { padding-left: 12px; width: 114px; }
  .spec-table td.std { text-align: center; }
  .spec-table tr.tall td { height: 40px; line-height: 23px; }
  .spec-table tr.first td { padding-top: 3px; }
  .spec-end { border-top: 1px solid var(--rule); margin-top: 3px; }
  .spec-note { font-size: 12.4px; text-align: right; margin-top: 8px; padding-right: 12px; word-spacing: 2px; }

  .footer-bar { position: absolute; left: 0; top: 1152px; width: 848px; height: 29px; }
  .footer-yellow { position: absolute; left: 0; top: 0; width: 320px; height: 29px; background: var(--yellow); }
  .footer-dark { position: absolute; left: 320px; top: 0; width: 528px; height: 29px; background: var(--dark); }
  .page-number { position: absolute; left: 52px; top: 5px; font-size: 16px; }
  .footer-mark {
    position: absolute; left: 306px; top: -4px; width: 36px; height: 36px;
    border-radius: 50%; background: #fff; border: 3px solid var(--dark);
  }
  .tagline {
    position: absolute; right: 52px; top: 2px; color: var(--yellow);
    font-family: "Playfair Display", Georgia, serif; font-style: italic; font-weight: 900; font-size: 17px;
  }
</style>
</head>
<body>
<div class="page">
  <div class="header-series">4” QM PUMPS SERIES</div>
  <div class="header-title">CROSS SECTIONAL DRAWING</div>

  <div class="section-drawing" role="img" aria-label="Cross sectional technical drawing of the 4 inch QM pump with numbered part callouts"></div>

  <section class="spec">
    <h1 class="spec-title">Material Specification-4” Pumps</h1>
    <table class="spec-table">
      <thead>
        <tr><th>Pos.</th><th>Components</th><th>Material</th><th>Standard</th></tr>
      </thead>
      <tbody>
        <tr class="first"><td class="pos">01</td><td class="comp">Discharge</td><td class="mat">Stainless Steel</td><td class="std">304</td></tr>
        <tr class="shaded"><td class="pos">12</td><td class="comp">Diffuser</td><td class="mat">Stainless Steel</td><td class="std">304</td></tr>
        <tr><td class="pos">18</td><td class="comp">Impeller</td><td class="mat">Stainless Steel</td><td class="std">304</td></tr>
        <tr class="shaded"><td class="pos">21</td><td class="comp">Split Cone</td><td class="mat">Stainless Steel</td><td class="std">304</td></tr>
        <tr><td class="pos">22</td><td class="comp">Split Cone Nut</td><td class="mat">Stainless Steel</td><td class="std">304</td></tr>
        <tr class="shaded tall"><td class="pos">24</td><td class="comp">Stop Ring</td><td class="mat">Carbon/<br>Graphite/PTFE</td><td class="std"></td></tr>
        <tr><td class="pos">32</td><td class="comp">Neck Ring Retainer</td><td class="mat">Stainless Steel</td><td class="std">304</td></tr>
        <tr class="shaded"><td class="pos">34</td><td class="comp">Strainer</td><td class="mat">Stainless Steel</td><td class="std">304</td></tr>
        <tr><td class="pos">36</td><td class="comp">Suction Interconnector</td><td class="mat">Stainless Steel</td><td class="std">304</td></tr>
        <tr class="shaded"><td class="pos">40</td><td class="comp">Pump Shaft</td><td class="mat">Stainless Steel</td><td class="std">431</td></tr>
        <tr><td class="pos">37</td><td class="comp">Coupling</td><td class="mat">Stainless Steel</td><td class="std">304</td></tr>
        <tr class="shaded"><td class="pos">47</td><td class="comp">Strap</td><td class="mat">Stainless Steel</td><td class="std">304</td></tr>
        <tr><td class="pos">52</td><td class="comp">Cable Guard</td><td class="mat">Stainless Steel</td><td class="std">304</td></tr>
        <tr class="shaded"><td class="pos">87</td><td class="comp">Neck Ring</td><td class="mat">SUS304+NBR</td><td class="std"></td></tr>
        <tr><td class="pos">88</td><td class="comp">Nut</td><td class="mat">Stainless Steel</td><td class="std">304</td></tr>
        <tr class="shaded"><td class="pos">89</td><td class="comp">Bearing</td><td class="mat">NBR</td><td class="std"></td></tr>
      </tbody>
    </table>
    <div class="spec-end"></div>
    <p class="spec-note">*AISI 316 stainless steel pumps are available on request.</p>
  </section>

  <footer class="footer-bar">
    <div class="footer-yellow"></div>
    <div class="footer-dark"></div>
    <span class="page-number">04</span>
    <span class="footer-mark" aria-hidden="true"></span>
    <span class="tagline">Made With Pride</span>
  </footer>
</div>
</body>
</html>
```